New brand for digital company - your chance to get creative

We need to create a brand for our new business 'Lanternfield Digital'. Please read the brief below before progressing as we are looking for some quite specific outputs.

Background

We are positioning ourselves as ‘marketing technologists’ - we're helping businesses engage with their customers in the online space.

Our tactics include branding, marketing, online management, and social media, however we are differentiating ourselves by focusing on overall strategy, not just tactics. Our tagline is ‘Online made simple’.

We have stipulated some parameters for the brand but otherwise want designers to exercise their creativity.

Requirements
Must have
• We want to see an entire concept, not just a logo.

```html
<!DOCTYPE html>
<html lang="en">
<head>
<meta charset="utf-8">
<title>Lanternfield Digital – Brand Concept</title>
<link rel="stylesheet" href="https://fonts.googleapis.com/css2?family=Exo:wght@300;400;600;700&display=swap">
<style>
  :root {
    --brand-green: #8bc653;
    --ink: #111111;
    --paper: #ffffff;
    --stage: #e8e8e8;
    --photo-dark: #1c1b1a;
    --photo-mid: #3a342e;
    --photo-warm: #6b4a33;
    --rule: #cfe4b8;
  }
  * { margin: 0; padding: 0; box-sizing: border-box; }
  html, body { width: 1200px; height: 1000px; overflow: hidden; }
  body {
    background: var(--stage);
    font-family: "Exo", sans-serif;
    position: relative;
  }

  /* ---------- Poster ---------- */
  .poster {
    position: absolute; left: 50px; top: 42px;
    width: 688px; height: 913px;
    overflow: hidden; color: var(--paper);
  }
  .poster__photo {
    position: absolute; inset: 0;
    background:
      radial-gradient(ellipse at 70% 35%, var(--photo-warm) 0%, transparent 45%),
      linear-gradient(180deg, var(--photo-mid) 0%, var(--photo-dark) 55%, #2a2724 100%);
  }
  .poster__brand {
    position: absolute; left: 30px; top: 146px;
    display: flex; align-items: center; gap: 10px;
    font-size: 26px; font-weight: 400; color: var(--brand-green);
  }
  .brand-square {
    width: 16px; height: 16px; background: var(--brand-green);
  }
  .poster__headline { position: absolute; left: 30px; top: 241px; }
  .headline-line {
    display: table; background: var(--brand-green);
    color: var(--paper); padding: 0 14px 0 2px;
    margin-bottom: 14px; line-height: 1;
  }
  .headline-line--light { font-weight: 300; font-size: 62px; padding-top: 2px; padding-bottom: 4px; }
  .headline-line--bold { font-weight: 700; font-size: 58px; padding-top: 4px; padding-bottom: 6px; }

  .poster__intro {
    position: absolute; left: 30px; top: 608px; width: 420px;
    font-size: 18px; font-weight: 300; line-height: 22px;
  }
  .poster__intro strong { color: var(--brand-green); font-weight: 600; }
  .poster__tagline { margin-top: 20px; }

  .poster__rule {
    position: absolute; left: 30px; right: 30px; top: 816px;
    border-top: 2px dotted rgba(255,255,255,0.7);
  }
  .poster__footer {
    position: absolute; left: 30px; top: 837px;
    display: flex; gap: 48px; font-size: 10px; line-height: 12.5px;
  }
  .footer-col { width: 112px; }
  .footer-col h3 { font-size: 10px; font-weight: 700; }
  .footer-col p { font-weight: 300; }
  .footer-col--contact { width: 200px; }

  /* ---------- Type specimen card ---------- */
  .specimen {
    position: absolute; left: 590px; top: 64px;
    width: 566px; height: 424px;
    background: var(--paper); color: var(--ink);
    padding: 0 23px;
  }
  .specimen__brand {
    position: absolute; left: 23px; top: 96px;
    display: flex; align-items: center; gap: 8px;
    font-size: 17px; font-weight: 400; color: var(--ink);
  }
  .specimen__brand .brand-square { width: 11px; height: 11px; background: var(--ink); }
  .specimen__rule {
    position: absolute; left: 23px; right: 23px; top: 131px;
    border-top: 1px dotted var(--rule);
  }
  .spec-label { font-size: 11px; color: var(--brand-green); font-weight: 400; }
  .spec-label span { color: var(--ink); }
  .specimen__headline { position: absolute; left: 23px; top: 156px; }
  .specimen__headline .spec-label { margin-bottom: 8px; }
  .spec-line {
    display: table; background: var(--brand-green); color: var(--paper);
    font-size: 35px; font-weight: 400; line-height: 38px;
    padding: 0 6px 0 1px; margin-bottom: 6px;
  }
  .specimen__styles {
    position: absolute; left: 23px; top: 336px;
    display: flex;
  }
  .spec-style { width: 176px; }
  .spec-style .spec-label { margin-bottom: 12px; }
  .spec-sample { font-size: 11px; line-height: 12px; }
  .spec-sample--sub b { font-weight: 600; }
  .spec-sample--body { font-size: 6px; line-height: 7.5px; }
  .spec-sample--caption { font-size: 4.5px; line-height: 5px; color: #555; }

  /* ---------- Brand square ---------- */
  .brand-tile {
    position: absolute; left: 765px; top: 506px;
    width: 392px; height: 452px;
    background: var(--brand-green);
    display: flex; align-items: center; justify-content: center;
  }
  .brand-tile__name {
    display: flex; align-items: center; gap: 10px;
    font-size: 24px; font-weight: 400; color: var(--paper);
    margin-top: 118px;
  }
  .brand-tile__name .brand-square { background: var(--paper); }
</style>
</head>
<body>

  <section class="poster">
    <div class="poster__photo" role="img" aria-label="Photograph of a dim creative studio with a pendant lamp, timber wall and a person seated in a lounge chair"></div>

    <div class="poster__brand"><span class="brand-square"></span>Lanternfield Digital</div>

    <h1 class="poster__headline">
      <span class="headline-line headline-line--light">We Are</span>
      <span class="headline-line headline-line--bold">Lanternfield</span>
      <span class="headline-line headline-line--light">Digital</span>
    </h1>

    <div class="poster__intro">
      <p>We specialise in <strong>branding, marketing, online management,</strong> and <strong>social media,</strong> however we differenciate ourselves by focusing on overall strategy, not just tactics.</p>
      <p class="poster__tagline">We are...<strong>online made simple</strong></p>
    </div>

    <div class="poster__rule"></div>

    <footer class="poster__footer">
      <div class="footer-col">
        <h3>Address</h3>
        <p>1 Street Name<br>Town, City<br>Zip Code, Country</p>
      </div>
      <div class="footer-col footer-col--contact">
        <h3>Contact</h3>
        <p>+61 (02) 5550 0142<br>www.lanternfielddigital.com<br>hello@lanternfielddigital.com</p>
      </div>
    </footer>
  </section>

  <section class="specimen">
    <div class="specimen__brand"><span class="brand-square"></span>Lanternfield Digital</div>
    <div class="specimen__rule"></div>

    <div class="specimen__headline">
      <p class="spec-label">Headline <span>(72 /84.4px)</span></p>
      <span class="spec-line">abcdefghijklmnopqrstuvwxy</span>
      <span class="spec-line">ABCDEFGDEFGHIJKLIMN</span>
      <span class="spec-line">0123456789!@£$</span>
    </div>

    <div class="specimen__styles">
      <div class="spec-style">
        <p class="spec-label">Subheader <span>(21 /24px)</span></p>
        <p class="spec-sample spec-sample--sub"><b>abcdefghijklmnopqrstuvwxyz</b><br>ABCDEFGHIJKVWXYZ<br>0123456789!@£$</p>
      </div>
      <div class="spec-style">
        <p class="spec-label">BodyCopy <span>(12 /15px)</span></p>
        <p class="spec-sample spec-sample--body"><b>abcdefghijklmnopqrstuvwxyz</b><br>ABCDEFGHIJKLMNOPQRSTUVWXYZ<br>0123456789!@£$</p>
      </div>
      <div class="spec-style">
        <p class="spec-label">Caption <span>(8/9px)</span></p>
        <p class="spec-sample spec-sample--caption">abcdefghijklmnopqrstuvwxyz<br>ABCDEFGHIJKLMNOPQRSTUVWXYZ<br>0123456789!@£$</p>
      </div>
    </div>
  </section>

  <section class="brand-tile">
    <div class="brand-tile__name"><span class="brand-square"></span>Lanternfield Digital</div>
  </section>

</body>
</html>
```